Yoga By Mirelle Ad for print

I need a print ad designed to go in a brochure for a charity event. I've attached the specs. I need the specs for the 1/2 page ad.
Text for ad:

“E-RYT 200 extensive training with Kestrel Path
Social Media Influencer
Offering group, private and corporate yoga classes
Email: info@yogabymirelle.example
Web: www.yogabymirelle.example
Phone: 555-201-3864
Instagram: @sunlitmatcurls

Target Market(s)

Yoga practitioners and businesses looking to bring yoga in to their operation.

Font styles to use
Serif
Script

Colors
eda3c7
e34197
eea4c8
f9d9e8
feeeee
000000
1b1b1b
cbcbcb
eaeaea

Requirements
Must have
• One version of my logo, I have provided many to choose from for best aesthetic appeal

```html
<!DOCTYPE html>
<html lang="en">
<head>
<meta charset="utf-8">
<title>Yoga By Mirelle – Half Page Ad</title>
<link href="https://fonts.googleapis.com/css2?family=Montserrat:wght@300;400;600;800&family=Cormorant+Garamond:wght@500;600&family=Great+Vibes&display=swap" rel="stylesheet">
<style>
  :root{
    --pink-hot:#e34197;
    --pink-coral:#e5566f;
    --pink-band:#f6c8d8;
    --pink-soft:#f9d9e8;
    --pink-blush:#feeeee;
    --ink:#1b1b1b;
    --black:#000000;
    --grey:#cbcbcb;
    --grey-light:#eaeaea;
    --teal:#7fd3dc;
    --teal-deep:#52bccb;
  }
  html,body{margin:0;padding:0;overflow:hidden;background:#fff;}
  .ad{
    position:relative;width:857px;height:1200px;overflow:hidden;
    background:linear-gradient(180deg,var(--pink-soft) 0%,var(--pink-blush) 55%,#fff5f8 80%,var(--pink-soft) 100%);
    font-family:"Montserrat",sans-serif;color:var(--ink);
  }
  .diagonal-band{position:absolute;left:0;top:0;width:857px;height:907px;}
  .hero-photo{
    position:absolute;left:40px;top:34px;width:385px;height:572px;
    border-radius:150px 150px 190px 190px / 120px 120px 90px 90px;
    background:radial-gradient(ellipse at 50% 40%,#f3c7a8 0%,#f4b7a0 35%,#5aa9c4 75%,rgba(90,169,196,0.0) 100%);
  }
  .brand-badge{
    position:absolute;left:499px;top:33px;width:224px;height:224px;border-radius:50%;
    background:linear-gradient(160deg,#ffffff 0%,var(--grey-light) 55%,var(--grey) 100%);
    border:4px solid #8a8a8a;box-sizing:border-box;
    display:flex;align-items:center;justify-content:center;
  }
  .brand-name{font-family:"Montserrat",sans-serif;font-weight:600;font-size:28px;color:var(--pink-coral);letter-spacing:0.5px;}
  .headline{position:absolute;left:520px;top:284px;width:320px;}
  .headline .cred{margin:0;font-weight:800;font-size:60px;line-height:1;letter-spacing:-1px;color:var(--ink);}
  .headline .training{margin:12px 0 0;font-weight:600;font-size:34.5px;line-height:1;color:var(--ink);}
  .headline .with{margin:10px 0 0;font-weight:400;font-size:34px;line-height:1;color:var(--ink);}
  .headline .partner{font-weight:800;color:var(--pink-coral);}
  .role{position:absolute;left:464px;top:547px;margin:0;font-weight:600;font-size:27px;color:var(--pink-coral);}
  .offer{position:absolute;left:515px;top:586px;margin:0;font-weight:300;font-size:21.5px;line-height:34px;color:var(--ink);letter-spacing:0.5px;}
  .social{position:absolute;left:162px;top:626px;display:flex;align-items:center;gap:8px;font-size:16px;font-weight:400;color:#444;}
  .social .dot{width:30px;height:30px;border-radius:50%;background:var(--pink-hot);}
  .pose{
    position:absolute;top:672px;width:214px;height:214px;border-radius:50%;
    border:5px solid #6d6d6d;box-sizing:border-box;
  }
  .pose.studio{background:radial-gradient(circle at 50% 45%,#c9a79d 0%,#d46a6e 45%,#c9474f 100%);}
  .pose.outdoor{background:linear-gradient(180deg,#6c9bd6 0%,#b9d2ee 55%,#d6cfc6 70%,#5d8a3c 85%,#48732c 100%);}
  .pose.one{left:62px}.pose.two{left:324px}.pose.three{left:587px}
  .gala-banner{
    position:absolute;left:0;top:907px;width:857px;height:230px;
    background:radial-gradient(ellipse at 30% 40%,#a9e3e8 0%,var(--teal) 50%,var(--teal-deep) 100%);
  }
  .gala-identity{position:absolute;left:18px;top:52px;width:230px;text-align:center;font-family:"Cormorant Garamond",serif;color:var(--ink);}
  .gala-name{margin:0;font-size:36px;font-weight:600;line-height:1;}
  .gala-benefit{margin:10px 0 0;font-size:14px;color:#555;border-top:1px solid #777;padding-top:3px;}
  .gala-cause{margin:2px 0 0;font-size:19px;font-weight:500;}
  .gala-sponsor{margin:10px 0 0;font-size:12px;}
  .gala-sponsor .sponsor-name{font-family:"Montserrat",sans-serif;font-weight:800;font-size:22px;color:#d8262e;margin-left:6px;}
  .gala-illustration{
    position:absolute;left:252px;top:0;width:390px;height:230px;
    background:linear-gradient(90deg,#5b3a80 0%,#2f3548 40%,#3d8f9a 60%,#a3588f 100%);
  }
  .gala-details{position:absolute;left:618px;top:14px;width:225px;text-align:right;}
  .gala-tagline{margin:0;font-family:"Great Vibes",cursive;font-size:37px;line-height:38px;color:#fff;}
  .gala-when{margin:14px 0 0;font-family:"Cormorant Garamond",serif;font-weight:600;font-size:20px;line-height:26px;color:var(--ink);}
  .gala-org{margin:14px 0 0;font-family:"Montserrat",sans-serif;font-size:13px;font-weight:400;line-height:1.2;color:var(--ink);}
  .contact-bar{
    position:absolute;left:0;top:1137px;width:857px;height:63px;
    background:linear-gradient(180deg,#fbe4ec,var(--pink-band));
    display:flex;align-items:center;justify-content:center;gap:26px;
    font-size:17px;font-weight:600;color:var(--black);
  }
  .contact-item{display:flex;align-items:center;gap:9px;}
  .contact-item svg{width:20px;height:20px;}
</style>
</head>
<body>
<div class="ad">
  <svg class="diagonal-band" viewBox="0 0 857 907" aria-hidden="true">
    <polygon points="0,255 857,125 857,470 0,515" fill="#f6c8d8"/>
  </svg>

  <div class="hero-photo" role="img" aria-label="Photo of the instructor seated cross-legged, arms stretched overhead"></div>

  <div class="brand-badge"><span class="brand-name">Sunlit Mat</span></div>

  <div class="headline">
    <p class="cred">E-RYT 200</p>
    <p class="training">Extensive Training</p>
    <p class="with">with <span class="partner">Kestrel Path</span></p>
  </div>

  <p class="role">Social Media Influencer</p>
  <p class="offer">Offering Group, Private<br>Corporate Yoga Classes</p>

  <div class="social"><span class="dot"></span><span>@sunlitmatcurls</span></div>

  <div class="pose studio one" role="img" aria-label="Photo of a kneeling yoga pose against a red wall"></div>
  <div class="pose studio two" role="img" aria-label="Photo of an eagle pose against a red wall"></div>
  <div class="pose outdoor three" role="img" aria-label="Photo of a dancer pose outdoors under a blue sky"></div>

  <section class="gala-banner">
    <div class="gala-identity">
      <p class="gala-name">Vine Voices Gala</p>
      <p class="gala-benefit">Benefiting</p>
      <p class="gala-cause">New Bloom Women's Fund</p>
      <p class="gala-sponsor">Presented by<span class="sponsor-name">PawHaven</span></p>
    </div>
    <div class="gala-illustration" role="img" aria-label="Illustration of three stylish women in gowns"></div>
    <div class="gala-details">
      <p class="gala-tagline">Helping women<br>help themselves</p>
      <p class="gala-when">Saturday, September 15, 2018<br>11 AM at the Maison Aurelle</p>
      <p class="gala-org">New Bloom<br>Women's Fund</p>
    </div>
  </section>

  <footer class="contact-bar">
    <span class="contact-item">
      <svg viewBox="0 0 24 24"><path d="M6.6 2.5l3 3.2-1.8 2.6c1.2 2.7 3.3 4.8 6 6l2.6-1.8 3.2 3-2 3.5C10 18.5 5.5 14 4.5 4.5z" fill="none" stroke="#000" stroke-width="2" stroke-linejoin="round"/></svg>
      555-201-3864
    </span>
    <span class="contact-item">
      <svg viewBox="0 0 24 24"><rect x="2" y="5" width="20" height="14" fill="none" stroke="#000" stroke-width="2"/><path d="M2 5l10 8 10-8" fill="none" stroke="#000" stroke-width="2"/></svg>
      info@yogabymirelle.example
    </span>
    <span class="contact-item">
      <svg viewBox="0 0 24 24"><circle cx="12" cy="12" r="9.5" fill="none" stroke="#000" stroke-width="2"/><ellipse cx="12" cy="12" rx="4" ry="9.5" fill="none" stroke="#000" stroke-width="1.6"/><path d="M2.5 12h19M4 7.5h16M4 16.5h16" stroke="#000" stroke-width="1.4"/></svg>
      www.yogabymirelle.example
    </span>
  </footer>
</div>
</body>
</html>
```